Business Card Design Project : Ferncliff Media

In preparation for market launch, Whistler's Ferncliff Media require the development of a business card. Ferncliff Media is a Community online publishing web portal. We provide the the city of Whistler located in B.C. (Canada) business directories, News, Classified ads, News, Events and blogs etc.

The main focus of the brand is to help local businesses to corporate with their online advertisement and marketing. Meeting our clients face to face is a must (B2B).

Target Market(s)

The target market is B2B customers. Business Owners to Marketing, advertising Managers

Industry/Entity Type

Business

Requirements
Must have
• - The business card will be two sided.
the BACK side will have our logo which consist of (icon, url,slogan) submited. The logo will be middle and centred.

The FRONT side should have company details:

Company Legal Name: TALLPINE FERNCLIFF MEDIA

Dale Morrow
Director of Sales & Marketing

www.tallpineferncliff.biz
dale@tallpineferncliff.biz

Phone: 604 555 0138
#2217 - 581 E. Harlow Ave.
Vancouver, B.C. V6N2K4 Canada
Nice to have
• - For the "FRONT" side of our business card. You can separate or re-arrange with our logo components (icon, logo,slogan). It does not have to be together.

Also our company legal name is rather long so arrange or organize the name in a way to make it shorter. Your experience and creativity will have to come in play.
Should not have
• should not have other colors beside logo color and black text (2 colors). Also nothing Three dimensional

```html
<!DOCTYPE html>
<html lang="en">
<head>
<meta charset="utf-8">
<title>Tallpine Ferncliff Media – Business Card</title>
<link rel="stylesheet" href="https://fonts.googleapis.com/css2?family=Source+Sans+3:wght@400;600;700&display=swap">
<style>
  :root {
    --brand-blue: #137bcd;
    --paper: #ffffff;
    --backdrop: #4b4b4b;
  }
  * { margin: 0; padding: 0; box-sizing: border-box; }
  html, body {
    width: 1200px;
    height: 907px;
    overflow: hidden;
    background: var(--backdrop);
    font-family: "Source Sans 3", "Myriad Pro", Arial, sans-serif;
  }
  .stage { position: relative; width: 1200px; height: 907px; }

  .card {
    position: absolute;
    width: 586px;
    height: 357px;
    border-radius: 19px;
    overflow: hidden;
  }

  /* Back side */
  .card-back {
    left: 316px;
    top: 74px;
    background: var(--brand-blue);
    color: var(--paper);
    text-align: center;
  }
  .back-brand {
    position: absolute;
    left: 0; right: 0;
    top: 128px;
    font-size: 34px;
    font-weight: 700;
    letter-spacing: 1px;
    line-height: 1;
  }
  .back-url {
    position: absolute;
    left: 0; right: 0;
    top: 195px;
    font-size: 31px;
    font-weight: 700;
    letter-spacing: -0.3px;
    line-height: 1.2;
  }
  .back-slogan {
    position: absolute;
    left: 0; right: 0;
    top: 234px;
    font-size: 21px;
    font-weight: 400;
    line-height: 1.2;
  }

  /* Front side */
  .card-front {
    left: 314px;
    top: 472px;
    background: var(--paper);
  }
  .front-band {
    position: absolute;
    left: 0; top: 0; bottom: 0;
    width: 242px;
    background: var(--brand-blue);
  }
  .company-first {
    position: absolute;
    right: 10px;
    top: 80px;
    color: var(--paper);
    font-size: 26px;
    font-weight: 700;
    line-height: 1.2;
  }
  .band-brand {
    position: absolute;
    left: 18px;
    bottom: 24px;
    color: var(--paper);
    font-size: 28px;
    font-weight: 700;
    line-height: 1.05;
  }
  .front-details {
    position: absolute;
    left: 251px;
    top: 80px;
    color: var(--brand-blue);
  }
  .company-rest {
    font-size: 26px;
    font-weight: 700;
    line-height: 1.2;
  }
  .person-name {
    margin-top: 24px;
    font-size: 25px;
    font-weight: 700;
    line-height: 1.1;
  }
  .person-title {
    font-size: 17px;
    font-weight: 400;
    line-height: 1.3;
  }
  .contact {
    margin-top: 26px;
    font-size: 16px;
    font-weight: 400;
    line-height: 20.5px;
    font-style: normal;
  }
</style>
</head>
<body>
<main class="stage">
  <section class="card card-back" aria-label="Card back">
    <div class="back-brand">TALLPINE FERNCLIFF</div>
    <div class="back-url">www.tallpineferncliff.biz</div>
    <div class="back-slogan">Your information gateway</div>
  </section>

  <section class="card card-front" aria-label="Card front">
    <div class="front-band">
      <div class="company-first">TALLPINE</div>
      <div class="band-brand">TALLPINE<br>FERNCLIFF</div>
    </div>
    <div class="front-details">
      <div class="company-rest">FERNCLIFF MEDIA</div>
      <div class="person-name">DALE MORROW</div>
      <div class="person-title">Director of Sales &amp; Marketing</div>
      <address class="contact">
        #2217 - 581 E. Harlow Ave.<br>
        Vancouver, B.C. V6N2K4 Canada<br>
        Phone: 604 555 0138<br>
        dale@tallpineferncliff.biz
      </address>
    </div>
  </section>
</main>
</body>
</html>
```